I need a shopify website for a beauty brand that i am starting. The name of the brand is called "Korvi Beauty" i need the website to have a "Sleek Sexy And Mordern Design" preferable with a "Black Colour Scheme" i need the shopify store to be "Integrated With Instagram and Facebook" (@KorviBeauty on Instagram and Korvi Beauty On Facebook) ... I Also need to be able to "Easily to upload future products" (as ive only got three products at the moment) and i will also need to be "Able to capture emails to use for email marketing in the future as the brand grows "

```html
<!DOCTYPE html>
<html lang="en">
<head>
<meta charset="utf-8">
<title>Korvi Beauty</title>
<link rel="stylesheet" href="https://fonts.googleapis.com/css2?family=Lora:wght@400;500;700&display=swap">
<style>
:root{
  --ink:#141414;
  --panel:#1b1b1b;
  --footer:#111111;
  --white:#ffffff;
  --muted:#bdbdbd;
  --red:#e8112d;
  --hero-bg:#dcdcdc;
  --tile:#e6e6e6;
  --serif:'Lora', Georgia, serif;
}
*{box-sizing:border-box;margin:0;padding:0}
html,body{width:1200px;height:4087px;overflow:hidden}
body{background:var(--panel);font-family:var(--serif);color:var(--white);position:relative}
a{color:inherit;text-decoration:none}
.abs{position:absolute}

/* header */
.site-header{position:absolute;left:0;top:0;width:1200px;height:81px;background:var(--ink)}
.brand{position:absolute;left:144px;top:22px;display:flex;align-items:center;gap:10px;font-size:18px;font-weight:700;letter-spacing:2px;text-transform:uppercase}
.brand-square{width:12px;height:12px;background:var(--white)}
.main-nav{position:absolute;right:214px;top:31px;display:flex;gap:32px;font-size:13px;text-transform:uppercase}
.main-nav .active{color:var(--red)}
.cart{position:absolute;left:1018px;top:26px;width:26px;height:26px}
.cart-badge{position:absolute;left:1036px;top:19px;width:15px;height:15px;border-radius:50%;background:var(--red);font-size:9px;text-align:center;line-height:15px}

/* hero */
.hero{position:absolute;left:0;top:81px;width:1200px;height:576px;background:var(--hero-bg)}
.hero-photo{position:absolute;right:0;top:0;width:640px;height:576px;background:radial-gradient(ellipse at 55% 45%,#b07a5c 0%,#7a4c36 35%,rgba(60,40,30,.6) 60%,rgba(220,220,220,0) 80%)}
.hero-title{position:absolute;left:144px;top:183px;color:var(--ink);font-size:56px;font-weight:700;letter-spacing:6px;text-transform:uppercase}
.hero-sub{position:absolute;left:144px;top:276px;color:#333;font-size:20px}
.btn{display:block;position:absolute;background:var(--red);color:var(--white);font-size:13px;font-weight:700;text-transform:uppercase;text-align:center}
.hero .btn{left:144px;top:339px;width:145px;height:44px;line-height:44px}

/* category tiles */
.cat-tile{position:absolute;top:695px;width:445px;height:313px;display:flex;align-items:center;justify-content:center}
.cat-tile.one{left:144px;background:linear-gradient(180deg,#f4f4f4 0 40%,#3a1a1e 40% 100%)}
.cat-tile.two{left:610px;background:linear-gradient(90deg,#7a7670,#a47a62 60%,#2b2220)}
.cat-label{background:var(--ink);padding:0 30px;height:52px;line-height:52px;font-size:20px;text-transform:uppercase}

.section-title{position:absolute;left:0;width:1200px;text-align:center;font-size:40px;font-weight:500;text-transform:uppercase}

/* products */
.product{position:absolute;width:216px;text-align:center}
.product-img{width:216px;height:176px;background:var(--tile)}
.product-name{margin-top:22px;font-size:15px;font-weight:500;text-transform:uppercase}
.product-price{margin-top:9px;font-size:13px;color:var(--red)}

/* instagram */
.insta{position:absolute;width:216px;height:176px}

/* banner */
.banner{position:absolute;left:0;top:2557px;width:1200px;height:454px;background:linear-gradient(90deg,#2a1a18,#6a4436 30%,#3a2420 50%,#7a5040 72%,#201616);display:flex;flex-direction:column;align-items:center;justify-content:center}
.banner-name{font-size:48px;font-weight:700;letter-spacing:6px;text-transform:uppercase}

/* news */
.news-card{position:absolute;top:3177px;width:445px;height:313px}
.news-card.one{left:144px;background:linear-gradient(180deg,#4a2a60,#c2643e 45%,#2a1a1a 85%,#151515)}
.news-card.two{left:610px;background:linear-gradient(180deg,#9a8a86,#6e4a3e 45%,#2a1e1c 85%,#151515)}
.news-title{position:absolute;left:43px;top:252px;font-size:20px;font-weight:500;text-transform:uppercase}

/* perks */
.perk{position:absolute;top:3576px;width:300px;text-align:center}
.perk svg{display:block;margin:0 auto;width:26px;height:22px}
.perk-title{margin-top:15px;font-size:13px;font-weight:500;text-transform:uppercase}
.perk-text{margin-top:14px;font-size:10px;color:var(--muted)}

/* footer */
.site-footer{position:absolute;left:0;top:3749px;width:1200px;height:338px;background:var(--footer)}
.foot-heading{position:absolute;top:52px;font-size:16px;font-weight:500;text-transform:uppercase}
.quick-links{position:absolute;left:156px;top:100px;list-style:none;font-size:12px;color:var(--muted);line-height:25px}
.foot-brand{position:absolute;left:345px;top:72px;width:300px;text-align:center}
.foot-brand .name{font-size:26px;font-weight:700;letter-spacing:3px;text-transform:uppercase}
.foot-brand p{margin-top:26px;font-size:12px;line-height:19px;color:var(--muted)}
.news-text{position:absolute;left:722px;top:101px;font-size:12px;color:var(--muted)}
.signup{position:absolute;left:724px;top:143px;display:flex}
.signup .field{width:216px;height:42px;border:1px solid #3a3a3a;background:var(--ink);font-size:10px;line-height:40px;padding-left:24px}
.signup .btn{position:static;width:104px;height:42px;line-height:42px;font-size:14px}
.copyright{position:absolute;left:0;top:283px;width:1200px;text-align:center;font-size:12px;color:var(--muted)}
</style>
</head>
<body>

<header class="site-header">
  <a class="brand" href="#"><span class="brand-square"></span>Korvi Beauty</a>
  <nav class="main-nav">
    <a class="active" href="#">Home</a><a href="#">About</a><a href="#">Products</a><a href="#">News</a><a href="#">Contact us</a>
  </nav>
  <svg class="cart" viewBox="0 0 24 24" aria-label="Cart"><path d="M1 3h4l3 11h11l3-8H7" fill="none" stroke="#fff" stroke-width="2.4"/><circle cx="9" cy="19" r="2" fill="#fff"/><circle cx="18" cy="19" r="2" fill="#fff"/></svg>
  <span class="cart-badge">0</span>
</header>

<section class="hero">
  <div class="hero-photo" role="img" aria-label="Portrait of a model wearing lashes"></div>
  <h1 class="hero-title">Korvi Beauty</h1>
  <p class="hero-sub">Lorem ipsum dolor sit ame consectetur adipiscing</p>
  <a class="btn" href="#">Shop now</a>
</section>

<a class="cat-tile one" href="#" role="img" aria-label="Lash boxes and perfume product flat lay"><span class="cat-label">Commodo Co</span></a>
<a class="cat-tile two" href="#" role="img" aria-label="Close-up of a customer wearing lashes"><span class="cat-label">Duis Auteure</span></a>

<h2 class="section-title" style="top:1097px">Featured Products</h2>

<div class="product" style="left:144px;top:1211px"><div class="product-img" role="img" aria-label="Pair of false lashes"></div><div class="product-name">Product Name</div><div class="product-price">$56.74</div></div>
<div class="product" style="left:376px;top:1211px"><div class="product-img" role="img" aria-label="Pair of false lashes"></div><div class="product-name">Product Name</div><div class="product-price">$56.74</div></div>
<div class="product" style="left:608px;top:1211px"><div class="product-img" role="img" aria-label="Pair of false lashes"></div><div class="product-name">Product Name</div><div class="product-price">$56.74</div></div>
<div class="product" style="left:840px;top:1211px"><div class="product-img" role="img" aria-label="Pair of false lashes"></div><div class="product-name">Product Name</div><div class="product-price">$56.74</div></div>
<div class="product" style="left:144px;top:1482px"><div class="product-img" role="img" aria-label="Pair of false lashes"></div><div class="product-name">Product Name</div><div class="product-price">$56.74</div></div>
<div class="product" style="left:376px;top:1482px"><div class="product-img" role="img" aria-label="Pair of false lashes"></div><div class="product-name">Product Name</div><div class="product-price">$56.74</div></div>
<div class="product" style="left:608px;top:1482px"><div class="product-img" role="img" aria-label="Pair of false lashes"></div><div class="product-name">Product Name</div><div class="product-price">$56.74</div></div>
<div class="product" style="left:840px;top:1482px"><div class="product-img" role="img" aria-label="Pair of false lashes"></div><div class="product-name">Product Name</div><div class="product-price">$56.74</div></div>

<a class="btn" href="#" style="left:528px;top:1801px;width:145px;height:45px;line-height:45px">View all</a>

<h2 class="section-title" style="top:1915px">Follow us Instagram</h2>

<div class="insta" style="left:144px;top:2020px;background:linear-gradient(135deg,#8a6a4a,#c79a7a,#3a4a6a)" role="img" aria-label="Instagram post from @KorviBeauty"></div>
<div class="insta" style="left:376px;top:2020px;background:linear-gradient(135deg,#c08670,#8a5040)" role="img" aria-label="Instagram post from @KorviBeauty"></div>
<div class="insta" style="left:608px;top:2020px;background:linear-gradient(135deg,#5a5a5a,#6a4030,#2a2a2a)" role="img" aria-label="Instagram post from @KorviBeauty"></div>
<div class="insta" style="left:840px;top:2020px;background:linear-gradient(135deg,#3a3030,#5a3a30,#2a2020)" role="img" aria-label="Instagram post from @KorviBeauty"></div>
<div class="insta" style="left:144px;top:2212px;background:linear-gradient(135deg,#9a5a40,#5a2a20)" role="img" aria-label="Instagram post from @KorviBeauty"></div>
<div class="insta" style="left:376px;top:2212px;background:linear-gradient(135deg,#1a1520,#5a4a50,#201a1a)" role="img" aria-label="Instagram post from @KorviBeauty"></div>
<div class="insta" style="left:608px;top:2212px;background:linear-gradient(135deg,#c0703a,#8a4a2a)" role="img" aria-label="Instagram post from @KorviBeauty"></div>
<div class="insta" style="left:840px;top:2212px;background:linear-gradient(135deg,#c0a060,#8a5a40,#3a3020)" role="img" aria-label="Instagram post from @KorviBeauty"></div>

<a class="btn" href="#" style="left:528px;top:2444px;width:145px;height:43px;line-height:43px">Load more</a>

<section class="banner" role="img" aria-label="Two close-up portraits of models wearing lashes">
  <div class="banner-name">Korvi Beauty</div>
</section>

<h2 class="section-title" style="top:3080px">News</h2>

<article class="news-card one" role="img" aria-label="Model with colourful eye makeup"><h3 class="news-title">Lorem ipsum dolor sit</h3></article>
<article class="news-card two" role="img" aria-label="Model with winged eyeliner"><h3 class="news-title">Lorem ipsum dolor sit</h3></article>

<div class="perk" style="left:163px">
  <svg viewBox="0 0 26 22"><rect x="1" y="4" width="15" height="11" fill="#e8112d"/><path d="M16 8h5l4 4v3h-9z" fill="#e8112d"/><circle cx="6" cy="17" r="3" fill="#e8112d"/><circle cx="20" cy="17" r="3" fill="#e8112d"/></svg>
  <div class="perk-title">Free returns</div>
  <div class="perk-text">Returns within 30 days receive a full refund.</div>
</div>
<div class="perk" style="left:474px">
  <svg viewBox="0 0 26 22"><circle cx="13" cy="11" r="9" fill="none" stroke="#e8112d" stroke-width="2.4"/><ellipse cx="13" cy="11" rx="4" ry="9" fill="none" stroke="#e8112d" stroke-width="2"/><path d="M4 11h18M5 7h16M5 15h16" stroke="#e8112d" stroke-width="1.8"/></svg>
  <div class="perk-title">Wordwide shipping</div>
  <div class="perk-text">Ship anywhere, rates available at checkout.</div>
</div>
<div class="perk" style="left:761px">
  <svg viewBox="0 0 26 22"><path d="M4 15v-3a9 9 0 0 1 18 0v3" fill="none" stroke="#e8112d" stroke-width="2.6"/><rect x="3" y="13" width="5" height="7" rx="1.5" fill="#e8112d"/><rect x="18" y="13" width="5" height="7" rx="1.5" fill="#e8112d"/></svg>
  <div class="perk-title">24/7 Support</div>
  <div class="perk-text">Call us anytime at 1(800) 888 8888</div>
</div>

<footer class="site-footer">
  <h4 class="foot-heading" style="left:156px">Quick links</h4>
  <ul class="quick-links"><li>Home</li><li>About</li><li>Products</li><li>News</li><li>Contact us</li></ul>
  <div class="foot-brand">
    <div class="name">Korvi Beauty</div>
    <p>Lorem ipsum dolor sit amet, consectetur adipiscing elit, sed do eiusmod tempo incididunt ut laborre magna</p>
  </div>
  <h4 class="foot-heading" style="left:722px">Newsletter</h4>
  <p class="news-text">Excepteur sint occaecat cupidatat non proident</p>
  <form class="signup"><div class="field">Enter Email</div><a class="btn" href="#">Sign up</a></form>
  <p class="copyright">© 2021 Korvi Beauty.All rights reserved.Privacy &nbsp;|&nbsp; Terms of Use &nbsp;|&nbsp; Cookie preferences &nbsp;|&nbsp; AdChoices</p>
</footer>

</body>
</html>
```